Visitenkarten- und Briefpapier Design - Logo vorhanden!
Zielgruppe
Wir sind eine Projektentwicklungs GmbH die Grundstücke kauft, projektiert und wieder verkauft. Eine zukünftige GmbH ist für den Innenausbau von neuen Häusern (EFH,DHH,MFH) gedacht. Wir sind ebenfalls für den Vertrieb von Häusern tätig.
Unsere Zielgruppe sind Endkunden im Immobilienbereich die Grundstücke und/oder Häuser bis Schlüsselfertig kaufen möchten, sowie Grundstückseigentümer die verkaufen wollen.
Wir benötigen Visitenkarten UND Briefpapier.
Aufgabenstellung
Bitte vorhandenes Logo verwenden.
Briefpapier:
Es soll ein ansprechendes modernes Design sein. Wir lassen uns gerne überraschen und versuchen schnellstmöglich Feedback zu geben.
Visitenkarte:
Es soll ein ansprechendes modernes Design sein. Die Visitenkarte bitte mit 2 Seiten, auf der Rückseite könnten wir uns das Dunkle ZERANT Logo sehr gut vorstellen (nur Logo).

```html
<!DOCTYPE html>
<html lang="de">
<head>
<meta charset="utf-8">
<title>ZERANT Visitenkarte</title>
<link rel="stylesheet" href="https://fonts.googleapis.com/css2?family=Open+Sans:wght@400;700;800&display=swap">
<style>
  :root {
    --backdrop: #d8d4cd;
    --card-light: #f2f2f2;
    --card-dark: #22242f;
    --accent-green: #76a534;
    --text-dark: #1f2029;
    --text-light: #f4f4f4;
  }
  * { margin: 0; padding: 0; box-sizing: border-box; }
  html, body { width: 1200px; height: 842px; overflow: hidden; }
  body {
    background: var(--backdrop);
    font-family: "Open Sans", Arial, sans-serif;
    display: flex;
    align-items: center;
    justify-content: center;
    gap: 48px;
  }
  .card {
    position: relative;
    width: 540px;
    height: 350px;
    overflow: hidden;
    box-shadow: 0 6px 18px rgba(0,0,0,0.18);
  }
  .card-front { background: var(--card-light); }
  .card-back {
    background: var(--card-dark);
    display: flex;
    align-items: center;
    justify-content: center;
  }
  .front-panel {
    position: absolute;
    top: 0; right: 0;
    width: 250px; height: 250px;
  }
  .panel-brand {
    position: absolute;
    top: 70px; right: 0;
    width: 250px;
    text-align: center;
    color: var(--text-light);
    font-size: 26px;
    font-weight: 400;
    letter-spacing: 4px;
  }
  .contact-block {
    position: absolute;
    left: 44px; top: 92px;
    color: var(--text-dark);
  }
  .person-name {
    font-size: 19px;
    font-weight: 800;
    letter-spacing: 0.5px;
  }
  .company {
    margin-top: 16px;
    font-size: 11.5px;
    line-height: 1.35;
    letter-spacing: 1.2px;
  }
  .company strong { font-weight: 800; letter-spacing: 0.5px; }
  .contact-list { margin-top: 26px; list-style: none; font-size: 12.5px; letter-spacing: 0.6px; }
  .contact-row { display: flex; align-items: flex-start; gap: 10px; line-height: 1.45; }
  .contact-row + .contact-row { margin-top: 10px; }
  .contact-row.tight { margin-top: 0; }
  .icon { width: 12px; height: 12px; margin-top: 4px; flex: none; }
  .icon-spacer { width: 12px; flex: none; }
  .back-brand {
    display: flex;
    align-items: center;
    gap: 18px;
    color: var(--text-light);
    font-size: 56px;
    font-weight: 400;
    letter-spacing: 8px;
  }
  .brand-square { width: 18px; height: 18px; background: var(--accent-green); }
</style>
</head>
<body>
  <section class="card card-front" aria-label="Visitenkarte Vorderseite">
    <svg class="front-panel" viewBox="0 0 250 250" aria-hidden="true">
      <path d="M0 0 H250 V155 C170 170 90 190 20 232 L0 232 Z" fill="var(--card-dark)"/>
      <path d="M20 232 C90 190 170 170 250 155" fill="none" stroke="var(--accent-green)" stroke-width="4"/>
    </svg>
    <div class="panel-brand">ZERANT</div>

    <div class="contact-block">
      <p class="person-name">LENA BRANDT</p>
      <p class="company"><strong>ZERANT //</strong><br>PROJEKTENTWICKLUNGS GmbH</p>
      <ul class="contact-list">
        <li class="contact-row">
          <svg class="icon" viewBox="0 0 12 12" aria-hidden="true"><path d="M2.5 1 L4.5 3.2 L3.6 4.6 C4.3 6 5.9 7.6 7.4 8.4 L8.8 7.5 L11 9.5 L9.6 11 C5.5 10.6 1.4 6.5 1 2.4 Z" fill="var(--text-dark)"/></svg>
          <span>+49 (0) 321 640 18</span>
        </li>
        <li class="contact-row tight">
          <span class="icon-spacer"></span>
          <span>+49 (0) 321 640 18 27</span>
        </li>
        <li class="contact-row">
          <svg class="icon" viewBox="0 0 12 12" aria-hidden="true"><circle cx="6" cy="6" r="5" fill="none" stroke="var(--text-dark)" stroke-width="1.4"/><circle cx="6" cy="6" r="2" fill="none" stroke="var(--text-dark)" stroke-width="1.4"/></svg>
          <span>BRANDT@ZERANT.de</span>
        </li>
        <li class="contact-row tight">
          <svg class="icon" viewBox="0 0 12 12" aria-hidden="true"><circle cx="6" cy="6" r="5" fill="none" stroke="var(--text-dark)" stroke-width="1.1"/><ellipse cx="6" cy="6" rx="2.2" ry="5" fill="none" stroke="var(--text-dark)" stroke-width="1"/><path d="M1 6 H11" stroke="var(--text-dark)" stroke-width="1"/></svg>
          <span>www.ZERANT.de</span>
        </li>
      </ul>
    </div>
  </section>

  <section class="card card-back" aria-label="Visitenkarte Rückseite">
    <div class="back-brand"><span class="brand-square"></span>ZERANT</div>
  </section>
</body>
</html>
```